MODELS AGENCY NEW YEAR 2026 CARD

A 10 cm x 21 cm horizontal New Year card for clients of our 2 models agencies, Pommelin (kids) and Velvaride (actors and adults) (logo in the jobs).

Side A of the card: creative mission:
-text: 2026
-text: Peace and Love
-Studio or movie set atmosphere
-tone of voice: optimistic, positive, colorful

Side B:
(name of 4 people of the agency:)
Odette, Anne-Sophie, Hortense & Luc-Antoine,
(2 logos)
Pommelin & VelvaRide
(Adres)
Rue des Tilleuls 74 b3 - 1200 Bruxelles - Belgique

Target Market(s)

Movie directors, photographers

Industry/Entity Type

Fashion, advertising & Movies

Requirements
Must have
• SEE TEXT IN BRIEFING

```html
<!DOCTYPE html>
<html lang="en">
<head>
<meta charset="UTF-8">
<title>New Year 2026 Card – Peace and Love</title>
<link rel="stylesheet" href="https://fonts.googleapis.com/css2?family=Amatic+SC:wght@400;700&display=swap">
<style>
  :root {
    --stripe-dark: #524d87;
    --stripe-light: #5b5694;
    --floor: #7c77b5;
    --floor-edge: #8c87c2;
    --floor-shadow: #6a65a3;
    --scene-deep: #36315f;
    --scene-mid: #5f5a99;
    --scene-soft: #9590cc;
    --photo-tone: #a9a5d6;
    --text-white: #ffffff;
  }

  * { margin: 0; padding: 0; box-sizing: border-box; }

  html, body {
    width: 1200px;
    height: 571px;
    overflow: hidden;
    background: var(--stripe-dark);
  }

  .card {
    position: relative;
    width: 1200px;
    height: 571px;
    overflow: hidden;
    background: repeating-linear-gradient(
      90deg,
      var(--stripe-light) 0 48px,
      var(--stripe-dark) 48px 96px
    );
  }

  .studio-floor {
    position: absolute;
    left: 0;
    top: 404px;
    width: 1200px;
    height: 167px;
    background: var(--floor);
    border-top: 8px solid var(--floor-edge);
  }

  .studio-scene {
    position: absolute;
    left: 30px;
    top: 60px;
    width: 545px;
    height: 425px;
    border-radius: 28px;
    background: linear-gradient(
      180deg,
      var(--scene-soft) 0%,
      var(--scene-mid) 18%,
      var(--scene-deep) 40%,
      var(--scene-deep) 78%,
      var(--floor-shadow) 100%
    );
  }

  .scattered-photos {
    position: absolute;
    left: 0;
    top: 480px;
    width: 1200px;
    height: 91px;
    background: linear-gradient(
      90deg,
      var(--photo-tone) 0 9%,
      transparent 9% 20%,
      var(--photo-tone) 20% 29%,
      transparent 29% 74%,
      var(--photo-tone) 74% 86%,
      transparent 86% 93%,
      var(--photo-tone) 93% 100%
    );
    opacity: 0.55;
  }

  .greeting {
    position: absolute;
    left: 660px;
    top: 122px;
    width: 450px;
    text-align: center;
    color: var(--text-white);
    font-family: "Amatic SC", cursive;
    font-weight: 700;
  }

  .greeting-year {
    display: block;
    font-size: 335px;
    line-height: 0.9;
    letter-spacing: 2px;
  }

  .greeting-wish {
    display: block;
    margin-top: -14px;
    font-size: 74px;
    line-height: 1;
    letter-spacing: 3px;
  }
</style>
</head>
<body>
  <main class="card">
    <div class="studio-floor"></div>
    <div class="studio-scene" role="img" aria-label="Illustration of a photo studio: a model in a pink dress posing before a dark backdrop, a photographer with a camera, a softbox light and a spotlight, with small sparkles"></div>
    <div class="scattered-photos" role="img" aria-label="Illustration of printed photographs scattered across the studio floor"></div>
    <h1 class="greeting">
      <span class="greeting-year">2026</span>
      <span class="greeting-wish">PEACE AND LOVE</span>
    </h1>
  </main>
</body>
</html>
```